Professional consulting firm needing a Word document template

I need a Word document template that can be used flexibly for a flyer or brochure of 1 to 3 pages in length. The first page should be designed in a way that it can stand alone as a one-page flyer without a formal cover page. I have attached sample text as a Word document that could be used as the basis for the first 1-2 pages, however I do need three page layouts designed to give flexibility to use as a 3 page booklet. I have attached our brand guidelines, logo, and some stock images that I have previously purchased (they may not all be useful but it gives some options). <br/>The Word document needs to be set up in away that it can easily be edited to accommodate updates to the text, and some variation in the quantity of text on each page. Each page should be able to accommodate a mixture of paragraph text, bullet points, small boxes to call out highlights, one or more images, and some white space to avoid clutter. It should look professional yet engaging and modern.

Font styles to use
Sans Serif

Requirements
Must have
• Must be an editable Microsoft Word document, using the text provided. Must be a layout suitable to use as 1 page, up to 3 pages. Must comply with brand guidelines.

```html
<!DOCTYPE html>
<html lang="en">
<head>
<meta charset="utf-8">
<title>Train Driver Competency Indicator Development Project – Brochure Template</title>
<link href="https://fonts.googleapis.com/css2?family=Source+Sans+3:wght@400;600;700&display=swap" rel="stylesheet">
<style>
:root{
  --navy:#24174f;
  --navy-deep:#1c1243;
  --purple:#8e3f91;
  --purple-soft:#a4539f;
  --teal:#2fc6c4;
  --sky:#1fb4e8;
  --ink:#2b2b33;
  --grey:#555a63;
  --label:#a9aeb6;
  --board:#fafbfc;
  --paper:#ffffff;
}
*{box-sizing:border-box;margin:0;padding:0}
html,body{width:1200px;height:1200px;overflow:hidden}
body{background:var(--board);font-family:"Source Sans 3",Arial,sans-serif;color:var(--ink);position:relative}
.page-label{position:absolute;top:280px;width:374px;text-align:center;font-size:24px;color:var(--label);font-weight:400;letter-spacing:.3px}
.page{position:absolute;top:362px;width:374px;height:530px;background:var(--paper);box-shadow:0 0 14px 6px rgba(150,160,175,.35);overflow:hidden}
.p1{left:20px}.p2{left:413px}.p3{left:805px}
.abs{position:absolute}

/* footer */
.footer{position:absolute;left:0;right:0;bottom:0;height:34px;background:linear-gradient(90deg,var(--navy-deep) 0%,var(--navy) 45%,var(--purple) 100%);display:flex;align-items:center;color:#fff;font-size:6.6px}
.footer-item{flex:1;display:flex;align-items:center;justify-content:center;gap:6px;height:100%}
.footer-item svg{width:12px;height:12px;flex:none}
.footer.divided .footer-item+.footer-item{border-left:1px solid rgba(255,255,255,.7);height:24px}

/* page 1 */
.brand-name{left:0;width:382px;top:22px;text-align:center;font-size:23px;font-weight:700;color:var(--navy);letter-spacing:1.2px}
.brand-dots{left:286px;top:-20px;width:100px;height:88px;border-radius:50%;background:radial-gradient(circle at 40% 40%,#dff6fb,#bfe9f2 60%,#eaf8fb)}
.hero-photo{left:0;top:79px;width:374px;height:211px;background:linear-gradient(160deg,#47c6c9 0%,#6fd0c8 25%,#c4e23c 45%,#e1443f 55%,#48b8d0 70%,#d7eef1 100%)}
.hero-title{left:58px;top:150px;width:264px;height:93px;background:rgba(146,66,150,.88);outline:1px solid #47c5e6;outline-offset:2px;color:#fff;font-size:15.5px;font-weight:600;text-align:center;display:flex;align-items:center;justify-content:center;line-height:1.15;padding:0 10px}
.p1-heading{left:29px;top:302px;font-size:10.3px;font-weight:700;color:var(--navy);border-left:5px solid var(--purple);padding-left:4px;line-height:14px}
.feature-tile{top:327px;width:99px;height:94px;background:linear-gradient(135deg,var(--teal),var(--sky))}
.feature-tile svg{position:absolute;left:30px;top:14px;width:40px;height:36px}
.feature-name{position:absolute;left:2px;right:2px;bottom:2px;height:22px;background:var(--navy);color:#fff;font-size:11.5px;display:flex;align-items:center;justify-content:center}
.feature-text{top:429px;width:92px;font-family:Arial,sans-serif;font-size:5.6px;line-height:7.2px;color:var(--ink)}
.p1-tagline{left:0;width:382px;top:475px;text-align:center;font-size:10.3px;font-weight:700;color:var(--navy)}

/* page 2 */
.title-rule{left:81px;top:34px;width:214px;height:3px;background:var(--navy)}
.doc-title{left:0;width:374px;top:44px;text-align:center;font-size:9.4px;font-weight:700;color:var(--ink)}
.body-copy{font-size:6.1px;line-height:8.4px;color:var(--grey)}
.competency-list{left:25px;top:98px;list-style:none;font-size:6.2px;line-height:8.45px;color:var(--ink)}
.competency-list li::before{content:"";display:inline-block;width:2.5px;height:2.5px;background:var(--ink);margin-right:6px;vertical-align:middle}
.bridge-photo{left:172px;top:97px;width:188px;height:95px;background:linear-gradient(180deg,#2a2440 0%,#4a3a62 40%,#6b4f6e 55%,#2b2b4a 70%,#151a30 100%);border:1px solid #1a1a2e}
.definition-box{top:212px;width:161px;height:90px;border:2px solid var(--navy);padding:4px 5px;font-size:6.6px;line-height:9.2px;color:var(--grey);text-align:justify}
.definition-box b{color:var(--ink);font-weight:700}
.highlight-callout{left:25px;top:314px;width:330px;height:49px;background:linear-gradient(90deg,#3bc7c2,#1db7e5);color:#fff;font-size:5.9px;line-height:8.4px;padding:7px 8px}
.section-head{left:12px;font-size:6.4px;font-weight:700;color:var(--ink);display:flex;align-items:center;gap:6px}
.section-head::before{content:"";width:6.5px;height:9px;background:var(--navy)}

/* page 3 */
.activity-box{width:145px;background:var(--navy);color:#fff;font-size:6.1px;line-height:8.3px;padding:7px 10px 0 16px}
.activity-box b{font-weight:700}
.activity-icon{width:26px;height:26px;border-radius:50%;background:var(--sky);border:1.5px solid #fff;display:flex;align-items:center;justify-content:center}
.activity-icon svg{width:13px;height:13px}
.pledge-box{left:43px;top:295px;width:287px;height:16px;border:1px solid var(--navy);font-size:6.1px;display:flex;align-items:center;justify-content:center;color:var(--ink)}
.social-title{left:0;width:374px;top:324px;text-align:center;font-size:6.2px;font-weight:700}
.social-button{top:344px;width:93px;height:25px;background:linear-gradient(90deg,var(--navy),var(--purple-soft));color:#fff;font-size:5.4px;display:flex;align-items:center;gap:7px;padding-left:8px}
.social-button i{width:6px;height:6px;border-radius:50%;background:#fff;flex:none}
</style>
</head>
<body>

<div class="page-label" style="left:20px">First Page</div>
<div class="page-label" style="left:413px">Second Page</div>
<div class="page-label" style="left:805px">Third Page</div>

<!-- Page 1 -->
<section class="page p1">
  <div class="abs brand-dots" role="img" aria-label="Decorative light blue dotted sphere"></div>
  <div class="abs brand-name">NORVANTA</div>
  <div class="abs hero-photo" role="img" aria-label="Photo of a train platform with colourful light trails"></div>
  <h1 class="abs hero-title">Train Driver Competency Indicator Development Project</h1>
  <h2 class="abs p1-heading">Heading TextLorem ipsum dolor sit amet, consectetur adipiscing elit.</h2>

  <div class="abs feature-tile" style="left:17px">
    <svg viewBox="0 0 40 36" fill="none" stroke="#fff" stroke-width="3" stroke-linecap="round" stroke-linejoin="round"><polyline points="3,30 14,19 21,25 35,10"/><polyline points="27,10 35,10 35,18"/></svg>
    <div class="feature-name">Growth</div>
  </div>
  <div class="abs feature-tile" style="left:138px">
    <svg viewBox="0 0 40 36" fill="none" stroke="#fff" stroke-width="3" stroke-linecap="round"><circle cx="16" cy="15" r="11"/><line x1="24" y1="23" x2="34" y2="33"/><polyline stroke-width="2" points="8,15 12,15 14,10 17,20 19,13 24,15"/></svg>
    <div class="feature-name">Research</div>
  </div>
  <div class="abs feature-tile" style="left:262px">
    <svg viewBox="0 0 40 36" fill="#fff"><rect x="14" y="3" width="12" height="6" rx="1.5" fill="none" stroke="#fff" stroke-width="2.5"/><rect x="2" y="9" width="36" height="24" rx="2"/><rect x="2" y="19" width="36" height="2" fill="#3bbde0"/><rect x="17" y="17" width="6" height="6" fill="#3bbde0"/></svg>
    <div class="feature-name">Portfolio</div>
  </div>
  <p class="abs feature-text" style="left:20px">Lorem ipsum dolor sit amet, consectetur adipiscing elit.</p>
  <p class="abs feature-text" style="left:142px">Maecenas eleifend fermentum ex. Vivamus sagittis ligula ipsum, ut lacinia orci placerat in.</p>
  <p class="abs feature-text" style="left:269px">Sed ut dui ut metus placerat rhoncus. Donec et commodo nisi, vel vehicula lectus.</p>
  <p class="abs p1-tagline">Text Lorem ipsum dolor sit amet, consectetur adipiscing elit.</p>

  <footer class="footer divided">
    <div class="footer-item"><svg viewBox="0 0 12 12"><path fill="#fff" d="M2.5 1l2 2.2-1 1.3c.6 1.4 1.6 2.4 3 3l1.3-1L10 8.5 9 10.5C5 10 2 7 1.5 3z"/></svg>5550142678</div>
    <div class="footer-item"><svg viewBox="0 0 12 12" fill="none" stroke="#fff"><rect x="1" y="2.5" width="10" height="7"/><polyline points="1,2.5 6,7 11,2.5"/></svg>hello@norvanta.com</div>
    <div class="footer-item"><svg viewBox="0 0 12 12" fill="none" stroke="#fff"><rect x="1" y="1.5" width="10" height="7"/><circle cx="6" cy="5" r="2"/><line x1="3" y1="10.5" x2="9" y2="10.5"/></svg>www.norvanta.com/au</div>
  </footer>
</section>

<!-- Page 2 -->
<section class="page p2">
  <div class="abs title-rule"></div>
  <h2 class="abs doc-title">Train Driver Competency Indicator Development Project</h2>
  <p class="abs body-copy" style="left:25px;top:64px;width:338px">We are commencing an applied research project to develop and test a framework of underlying core competencies for train driver performance. The objective of the project is to identify observable indicators that describe effective performance in the following types of underlying competencies:</p>
  <ul class="abs competency-list">
    <li>Application of Procedures</li>
    <li>Communication</li>
    <li>Operation of Tools / Equipment</li>
    <li>Problem Solving and Decision Making</li>
    <li>Route Knowledge</li>
    <li>Self Management</li>
    <li>Situation Awareness</li>
    <li>System Knowledge</li>
    <li>Teamwork and Leadership</li>
    <li>Train Handling</li>
    <li>Workload Management</li>
  </ul>
  <div class="abs bridge-photo" role="img" aria-label="Photo of a city bridge and skyline at night over water"></div>

  <div class="abs definition-box" style="left:27px"><b>Underlying competencies:</b><br>The underpinning knowledge and skills required by a train driver, to perform a range of different tasks effectively. Underlying competencies include both ‘technical’ and ‘non-technical’ skills. They are not specific to one driving task, but help build resilient performance across all tasks, conditions or situations that a driver may encounter.</div>
  <div class="abs definition-box" style="left:196px"><b>Underlying competencies:</b><br>The underpinning knowledge and skills required by a train driver, to perform a range of different tasks effectively. Underlying competencies include both ‘technical’ and ‘non-technical’ skills. They are not specific to one driving task, but help build resilient performance across all tasks, conditions or situations that a driver may encounter.</div>

  <div class="abs highlight-callout">In contrast to other performance marker systems, the current project aims to include both ‘technical’ and ‘non-technical’ skills in an integrated framework, with substantial input from drivers across the industry, both in passenger and freight operations. The aim is to develop a framework that uses a language that describes performance in a way that is relatable to drivers, trainers, and assessors.</div>

  <h3 class="abs section-head" style="top:368px">What are the benefits for participating organisations?</h3>
  <p class="abs body-copy" style="left:25px;top:386px;width:342px">All participating rail organisations will receive a copy of the performance indicator framework, which they are free to use or adapt for application within their own operation. A summary report will also be provided, outlining the methodology and aggregated results of the data collection activities. All results will be presented in a de-identified way, to ensure the anonymity of participating organisations and individuals.</p>
  <h3 class="abs section-head" style="top:427px">What is involved?</h3>
  <p class="abs body-copy" style="left:25px;top:445px;width:342px">Participating organisations will be invited to provide in-kind support for the following activities during the period April – June 2020:</p>

  <footer class="footer" style="height:36px">
    <div class="footer-item"><svg viewBox="0 0 12 12"><path fill="#fff" d="M2.5 1l2 2.2-1 1.3c.6 1.4 1.6 2.4 3 3l1.3-1L10 8.5 9 10.5C5 10 2 7 1.5 3z"/></svg>5550142678</div>
    <div class="footer-item"><svg viewBox="0 0 12 12" fill="none" stroke="#fff"><rect x="1" y="2.5" width="10" height="7"/><polyline points="1,2.5 6,7 11,2.5"/></svg>hello@norvanta.com</div>
    <div class="footer-item"><svg viewBox="0 0 12 12" fill="none" stroke="#fff"><rect x="1" y="1.5" width="10" height="7"/><circle cx="6" cy="5" r="2"/><line x1="3" y1="10.5" x2="9" y2="10.5"/></svg>www.norvanta.com/au</div>
  </footer>
</section>

<!-- Page 3 -->
<section class="page p3">
  <div class="abs activity-box" style="left:32px;top:29px;height:80px"><b>Interviews with volunteer Driver participants</b>: individual discussions with our researchers about drivers’ previous experiences, to gather information about expert driving strategies and positive techniques used in normal and abnormal operations.</div>
  <div class="abs activity-box" style="left:193px;top:29px;height:80px"><b>Initial workshop</b>: a facilitated group workshop to understand the links between underlying competencies and driving tasks, and to understand Drivers’ perceptions of what each underlying competency looks like in practice.</div>
  <div class="abs activity-box" style="left:32px;top:129px;height:85px"><b>Driver Training Survey</b>: a voluntary survey will be distributed, requesting Driver Trainers’ and Assessors’ views on the importance of underlying competencies in driving performance, and further data about expert strategies and techniques.</div>
  <div class="abs activity-box" style="left:193px;top:129px;height:85px"><b>Follow-up workshop</b>: a facilitated group workshop to test and refine the performance indicators. Where possible, indicators will be tested through participants providing ratings of a video sample of actual performance, to determine whether multiple raters can distinguish between competency categories.</div>

  <div class="abs activity-icon" style="left:20px;top:18px"><svg viewBox="0 0 13 13" fill="none" stroke="#fff" stroke-width="1.2"><polygon points="5,1 8,1 7.5,3 5.5,3"/><polygon points="5.5,3 7.5,3 8.5,10 6.5,12 4.5,10"/></svg></div>
  <div class="abs activity-icon" style="left:181px;top:18px"><svg viewBox="0 0 13 13" fill="none" stroke="#fff" stroke-width="1.2"><rect x="2.5" y="2" width="8" height="6"/><line x1="1" y1="10.5" x2="12" y2="10.5"/></svg></div>
  <div class="abs activity-icon" style="left:20px;top:117px"><svg viewBox="0 0 13 13" fill="none" stroke="#fff" stroke-width="1.2"><rect x="1.5" y="2.5" width="9" height="9"/><line x1="5" y1="8" x2="11.5" y2="1.5"/></svg></div>
  <div class="abs activity-icon" style="left:181px;top:117px"><svg viewBox="0 0 13 13" fill="none" stroke="#fff" stroke-width="1.2"><circle cx="6.5" cy="4.5" r="2.5"/><path d="M2 12c0-3 2-4.5 4.5-4.5S11 9 11 12z"/></svg></div>

  <p class="abs body-copy" style="left:24px;top:239px;width:338px">It is anticipated that workshops will be run in Brisbane, Sydney and Melbourne. We would appreciate support from participating organisations in providing a workshop venue where possible. Apart from the in-kind support of providing access to personnel and a meeting room, there is no cost associated with participation in the project.</p>
  <p class="abs body-copy" style="left:24px;top:273px;width:338px">In addition to the activities involving industry participation, we will also be completing a detailed task analysis and analysing incident reports and other publicly available data, to help inform the development of the framework.</p>
  <div class="abs pledge-box">We look forward to hearing from organisations interested in being part of this landmark project.</div>
  <p class="abs social-title">We are Social, Follow us on:</p>
  <div class="abs social-button" style="left:36px"><i></i>connect.net/norvanta</div>
  <div class="abs social-button" style="left:143px"><i></i>friendspace.net/norvanta</div>
  <div class="abs social-button" style="left:249px"><i></i>chirper.net/norvanta</div>

  <footer class="footer" style="height:36px">
    <div class="footer-item"><svg viewBox="0 0 12 12"><path fill="#fff" d="M2.5 1l2 2.2-1 1.3c.6 1.4 1.6 2.4 3 3l1.3-1L10 8.5 9 10.5C5 10 2 7 1.5 3z"/></svg>5550142678</div>
    <div class="footer-item"><svg viewBox="0 0 12 12" fill="none" stroke="#fff"><rect x="1" y="2.5" width="10" height="7"/><polyline points="1,2.5 6,7 11,2.5"/></svg>hello@norvanta.com</div>
    <div class="footer-item"><svg viewBox="0 0 12 12" fill="none" stroke="#fff"><rect x="1" y="1.5" width="10" height="7"/><circle cx="6" cy="5" r="2"/><line x1="3" y1="10.5" x2="9" y2="10.5"/></svg>www.norvanta.com/au</div>
  </footer>
</section>

</body>
</html>
```